Website for new dental office

I am Dr. Calvin Merrow and am building a new dental practice. I specialize in general dentistry. I am young and have a higher end dental practice incorporating very new technologies and would like my website to reflect that. As many dental patients are older, the website must be very easy to navigate. I would like patients to be able to request appointments, and will eventually add on patient information forms (the health history, etc, that you normally fill out in the practice) from my practice management software, so leave an area for that.

Industry/Entity Type

Building

```html
<!DOCTYPE html>
<html lang="en">
<head>
<meta charset="utf-8">
<title>Merrow Dental</title>
<link rel="stylesheet" href="https://fonts.googleapis.com/css2?family=Advent+Pro:wght@200;300;400&family=Tinos&family=Arimo:wght@700&display=swap">
<style>
  :root {
    --brand-blue: #3e48c8;
    --brand-blue-deep: #1e2270;
    --phrase-blue: #4a55d8;
    --nav-text: #f2efcf;
    --ink: #111111;
    --body-grey: #7a7a7a;
    --label-grey: #555555;
    --black: #000000;
    --white: #ffffff;
  }
  * { box-sizing: border-box; margin: 0; padding: 0; }
  html, body { width: 1200px; height: 922px; overflow: hidden; background: var(--white); }
  body { font-family: "Advent Pro", sans-serif; position: relative; }

  .site-header {
    position: absolute; left: 0; top: 0; width: 1200px; height: 154px;
    background: linear-gradient(to bottom, var(--brand-blue) 0%, #3238a8 45%, var(--brand-blue-deep) 100%);
  }
  .brand-name {
    position: absolute; left: 42px; top: 62px;
    font-family: "Tinos", serif; font-size: 27px; color: var(--white); font-weight: 400;
  }
  .slogan {
    position: absolute; left: 980px; top: 64px;
    font-family: "Tinos", serif; font-size: 24px; color: var(--brand-blue);
  }
  .slogan-rule {
    position: absolute; left: 978px; top: 103px; width: 222px; height: 1px; background: var(--brand-blue);
  }

  .main-nav {
    position: absolute; left: 0; top: 154px; width: 1200px; height: 80px; background: var(--black);
  }
  .main-nav ul { list-style: none; }
  .main-nav li {
    position: absolute; top: 24px;
    font-size: 24px; font-weight: 300; color: var(--nav-text); letter-spacing: 0.4px; white-space: nowrap;
  }
  .nav-team { left: 41px; }
  .nav-services { left: 132px; }
  .nav-portfolio { left: 282px; }
  .nav-office { left: 433px; }
  .nav-resources { left: 588px; }
  .nav-contact { left: 828px; }

  .hero {
    position: absolute; left: 0; top: 234px; width: 1200px; height: 383px; background: var(--black);
  }
  .hero-image {
    position: absolute; left: 156px; top: 58px; width: 930px; height: 172px;
    background: radial-gradient(ellipse at center, #1f2030 0%, #101018 55%, #000000 100%);
  }
  .promo-phrase {
    position: absolute; left: 41px; top: 82px;
    font-size: 64px; font-weight: 200; line-height: 72px; letter-spacing: 3px; color: var(--phrase-blue);
    white-space: nowrap;
  }

  .intro {
    position: absolute; left: 0; top: 617px; width: 1200px; height: 265px; background: var(--white);
  }
  .dentist-name { position: absolute; left: 49px; top: 29px; font-size: 26px; font-weight: 400; color: var(--brand-blue); }
  .dentist-name .credential { color: var(--label-grey); font-weight: 300; }
  .contact { position: absolute; left: 49px; top: 97px; font-size: 22px; line-height: 32px; color: var(--body-grey); font-weight: 300; }
  .contact b { color: var(--ink); font-weight: 400; }
  .appointment-button {
    position: absolute; left: 49px; top: 169px; width: 322px; height: 59px; border-radius: 4px;
    background: linear-gradient(to bottom, var(--brand-blue) 0%, var(--brand-blue-deep) 100%);
    color: var(--nav-text); font-size: 23px; font-weight: 400; text-align: center; line-height: 57px;
  }
  .description { position: absolute; left: 409px; top: 28px; width: 712px; }
  .description h2 { font-size: 27px; font-weight: 400; color: var(--ink); margin-bottom: 34px; }
  .description p { font-size: 22px; font-weight: 300; line-height: 31px; color: var(--body-grey); margin-bottom: 31px; }

  .site-footer {
    position: absolute; left: 0; top: 882px; width: 1200px; height: 40px; background: var(--black);
    font-family: "Arimo", sans-serif; font-weight: 700; font-size: 12px; color: var(--white);
    text-align: center; line-height: 36px;
  }
</style>
</head>
<body>
  <header class="site-header">
    <div class="brand-name">Merrow Dental</div>
    <div class="slogan">Care, made simple</div>
    <div class="slogan-rule"></div>
  </header>

  <nav class="main-nav">
    <ul>
      <li class="nav-team">TEAM</li>
      <li class="nav-services">SERVICES</li>
      <li class="nav-portfolio">PORTFOLIO</li>
      <li class="nav-office">OUR OFFICE</li>
      <li class="nav-resources">PATIENT RESOURCES</li>
      <li class="nav-contact">CONTACT US</li>
    </ul>
  </nav>

  <section class="hero">
    <div class="hero-image" role="img" aria-label="Photograph of the bright, modern treatment room at Merrow Dental"></div>
    <h1 class="promo-phrase">MODERN DENTISTRY,<br>GENTLE CARE</h1>
  </section>

  <section class="intro">
    <div class="dentist-name">Calvin Merrow <span class="credential">(DDS)</span></div>
    <div class="contact">
      <div><b>Phone</b> : 555-210-4417</div>
      <div><b>Email</b> : hello@merrowdental.com</div>
    </div>
    <div class="appointment-button">Request An Appointment</div>
    <div class="description">
      <h2>About Our Practice</h2>
      <p>Merrow Dental offers general dentistry for the whole family, using the newest digital imaging and gentle, precise tools. Every visit is unhurried and explained in plain words.</p>
      <p>Request a visit online, and complete your patient forms before you arrive.</p>
    </div>
  </section>

  <footer class="site-footer">Copyright : Calvin Merrow&nbsp;&nbsp; 2014</footer>
</body>
</html>
```